New Artwork/Design for Established Weight Loss Podcast

Hello,
I would like new artwork/design for my podcast. It's called Bright Path Slimdown and has been a consistently top 50 show in the fitness/nutrition category on Orbix. My current design was originally created when I started the podcast over 2 years ago. It's time to refresh and update things! I would like a new design that incorporates a photo of me, but could also be used as a standalone logo for the podcast without my photo. A nice, clean, professional, yet fun design. Here is a Vantor drive link with professional photos that could be used:
https://files.example-share.net/folders/7Qkrt58x-p2mLWHtabvPXsaQ9Ro6JwZ3k?usp=sharing

Here's a little more about the show . There are three big taglines. These do NOT need to be included on the design. I just include them here to help with the feel/theme of the design.

1: To change your body, you must first change your brain.
2: There's so much more to you than just a number (what you weigh).
3: Losing weight is really about gaining life and living the life you've always wanted.

This podcast is all about busy moms, dads, husbands, wives who are working, raising kids, and trying to juggle everything life’s throwing at them … but also want to be the best they can for their family and friends and loved ones.

The podcast is NOT about how to get six-pack abs or how to drop as much weight as possible in 8 weeks. It's about finding sustainable success with your body, peace of mind with food, and improving your relationship with yourself.

Week by week, I provide bite-sized guidance - 20-25 minute episodes that pull back the curtain and reveal the truth about what it takes to lose weight and gain life - what strategy and approach real people are using to get results while escaping the soul-sucking, all-or-nothing diet mentality.

Here's a link to the current artwork: https://files.example-share.net/file/d/4T2bHn8qsvkeTrmzYpRd-ab3KNJ-m-QXZ/view?usp=sharing

And the logo without my photo: https://files.example-share.net/file/d/8JN5pKa3Rw_h2b74cFxYqPmE6zGtdLs/view?usp=sharing

I'm open to any colors, but something that either matches the colors of my website or signature "Move Glow Trim Down" program would probably be a smart idea. Here are links to my website and the MGTD logo . . .

Website: https://danemarshwellness.example/

MGTD logo:
https://files.example-share.net/file/d/5VQpLm2Kxe_Tw9Hr4zNgUa7YcBfsjdP/view?usp=sharing

Happy to answer any questions you might have. Thanks.

Target Market(s)

35 to 55 years old, roughly 70% female, 30% male, professionals, primarily in the U.S. and Canada

Industry/Entity Type

nutrition, health, weight loss

Requirements
Must have
• One version with my photo and the same design without my photo
Nice to have
• Open to any colors, but possibly incorporate colors from either my website or MGTD logo (see project description for more info)
Should not have
• Any hardcore fitness or bodybuilding imagery

```html
<!DOCTYPE html>
<html lang="en">
<head>
<meta charset="utf-8">
<title>Bright Path Slimdown Podcast — Cover Art</title>
<link rel="stylesheet" href="https://fonts.googleapis.com/css2?family=League+Spartan:wght@700;800;900&display=swap">
<style>
  :root {
    --ink: #2a2734;
    --coral: #fe5a52;
    --white: #ffffff;
    --title-size: 192px;
  }
  * { margin: 0; padding: 0; box-sizing: border-box; }
  html, body {
    width: 1200px;
    height: 1200px;
    overflow: hidden;
    background: var(--ink);
  }
  .cover {
    position: relative;
    width: 1200px;
    height: 1200px;
    background: var(--ink);
    font-family: "League Spartan", "Arial Black", sans-serif;
    overflow: hidden;
  }
  .brand-name {
    position: absolute;
    left: 76px;
    top: 100px;
    display: flex;
    align-items: center;
    gap: 12px;
    font-weight: 800;
    font-size: 30px;
    letter-spacing: 0.04em;
    color: var(--coral);
  }
  .brand-name .dot {
    width: 14px;
    height: 14px;
    background: var(--coral);
    border-radius: 50%;
  }
  .corner-block {
    position: absolute;
    left: 1118px;
    top: 91px;
    width: 82px;
    height: 70px;
    background: var(--coral);
  }
  .title-line {
    position: absolute;
    left: 0;
    width: 1200px;
    display: flex;
    justify-content: center;
    align-items: center;
    font-weight: 800;
    font-size: var(--title-size);
    line-height: 1;
    height: 160px;
    letter-spacing: -0.01em;
  }
  .title-line--coral { color: var(--coral); }
  .title-line--white { color: var(--white); }
  .title-line--bright { top: 208px; }
  .title-line--path   { top: 377px; }
  .title-line--slim   { top: 543px; }
  .title-line--down   { top: 711px; }
  .brain-mark {
    display: inline-block;
    width: 132px;
    height: 136px;
    margin: 0 6px;
    background: var(--coral);
    border-radius: 46% 46% 40% 40%;
    transform: translateY(-8px);
  }
  .podcast-label {
    position: absolute;
    left: 0;
    top: 896px;
    width: 1200px;
    text-align: center;
    color: var(--white);
    font-weight: 700;
    font-size: 56px;
    line-height: 1;
    letter-spacing: 0.28em;
    padding-left: 0.28em;
  }
  .host-band {
    position: absolute;
    left: 249px;
    top: 1014px;
    width: 685px;
    height: 78px;
    background: var(--coral);
    display: flex;
    justify-content: center;
    align-items: center;
    gap: 16px;
  }
  .host-band .with {
    color: var(--ink);
    font-weight: 800;
    font-size: 42px;
    line-height: 1;
    transform: translateY(6px);
  }
  .host-band .host {
    color: var(--white);
    font-weight: 800;
    font-size: 62px;
    line-height: 1;
    transform: translateY(4px);
  }
</style>
</head>
<body>
  <main class="cover">
    <div class="brand-name"><span class="dot"></span>DANE MARSH</div>
    <div class="corner-block"></div>

    <h1 class="podcast-title" aria-label="Bright Path Slimdown">
      <span class="title-line title-line--coral title-line--bright">BRIGHT</span>
      <span class="title-line title-line--white title-line--path">PATH</span>
      <span class="title-line title-line--white title-line--slim">SLIM</span>
      <span class="title-line title-line--coral title-line--down">D<span class="brain-mark" role="img" aria-label="Brain icon standing in for the letter O"></span>WN</span>
    </h1>

    <p class="podcast-label">PODCAST</p>

    <div class="host-band">
      <span class="with">WITH</span>
      <span class="host">DANE MARSH</span>
    </div>
  </main>
</body>
</html>
```